Breezeway Climate Business Card Design

Design new, 2 sides, business cards for a residential and light commercial heating, air conditioning contractor.

Target Market(s)

Homeowners, small businesses

Industry/Entity Type

Business

Contact Information for Business Card

Dominic Vasquerelli
Phone - 555-214-6837
Email
Address - PO box 618
Millbrook NJ 07999
Website - www.BreezewayClimateLLC.example

Requirements
Must have
• logo, company colors, standard size with no die cut, so I can use printhaven

```html
<!DOCTYPE html>
<html lang="en">
<head>
<meta charset="utf-8">
<title>Breezeway Climate Business Card</title>
<link href="https://fonts.googleapis.com/css2?family=Roboto:wght@400;500;700&display=swap" rel="stylesheet">
<style>
  :root {
    --crimson: #b8253f;
    --crimson-deep: #9a1d33;
    --gold: #eba52a;
    --paper: #ffffff;
    --paper-shade: #ececec;
    --ink: #1d1d1d;
    --ink-soft: #4a4a4a;
    --backdrop: #e9e4dc;
  }
  * { margin: 0; padding: 0; box-sizing: border-box; }
  html, body {
    width: 1200px; height: 1023px; overflow: hidden;
    background: var(--backdrop);
    font-family: "Roboto", Arial, sans-serif;
  }
  .canvas { position: relative; width: 1200px; height: 1023px; }
  .card {
    position: absolute; left: 320px; width: 560px; height: 320px;
    border-radius: 16px; overflow: hidden;
    box-shadow: 0 8px 24px rgba(0,0,0,0.18);
  }
  .card-front { top: 120px; background: linear-gradient(135deg, var(--paper) 40%, var(--paper-shade)); }
  .card-back {
    top: 570px;
    background: radial-gradient(circle at 70% 30%, #c9304b, var(--crimson-deep) 80%);
    display: flex; align-items: center; justify-content: center;
  }
  .front-art { position: absolute; inset: 0; }
  .company-name { font-weight: 700; letter-spacing: 1px; text-transform: uppercase; }
  .front-brand {
    position: absolute; left: 34px; top: 128px;
    display: flex; align-items: center; gap: 10px;
    color: var(--crimson); font-size: 22px;
  }
  .brand-dot { width: 14px; height: 14px; border-radius: 50%; background: var(--gold); }
  .holder { position: absolute; left: 40px; top: 26px; width: 260px; text-align: right; }
  .holder-name { font-size: 24px; font-weight: 500; color: var(--ink); white-space: nowrap; }
  .holder-title { font-size: 12px; color: var(--crimson); margin-top: 2px; }
  .contacts {
    position: absolute; left: 40px; bottom: 24px;
    list-style: none; font-size: 12px; color: var(--ink-soft); line-height: 18px;
  }
  .contacts li { display: flex; align-items: center; gap: 8px; white-space: nowrap; }
  .contacts svg { width: 11px; height: 11px; flex: none; }
  .address {
    position: absolute; right: 22px; bottom: 24px; text-align: right;
    color: var(--paper); font-size: 12px; font-style: normal;
    line-height: 18px; letter-spacing: 0.5px; white-space: nowrap;
  }
  .back-brand {
    display: flex; align-items: center; gap: 14px;
    padding: 26px 40px; border: 3px solid var(--paper); border-radius: 14px;
    color: var(--paper); font-size: 36px;
  }
  .back-brand .brand-dot { width: 20px; height: 20px; }
</style>
</head>
<body>
<main class="canvas">
  <section class="card card-front" aria-label="Card front">
    <svg class="front-art" viewBox="0 0 560 320" aria-hidden="true">
      <defs>
        <linearGradient id="redPanel" x1="0" y1="0" x2="1" y2="1">
          <stop offset="0" stop-color="#c32f48"/>
          <stop offset="1" stop-color="#a21f37"/>
        </linearGradient>
      </defs>
      <path d="M300 0 C400 40 410 200 360 320 L560 320 L560 0 Z" fill="url(#redPanel)"/>
      <path d="M285 0 C385 40 395 200 345 320" fill="none" stroke="var(--gold)" stroke-width="5"/>
    </svg>
    <div class="holder">
      <div class="holder-name">Dominic Vasquerelli</div>
      <div class="holder-title">Title</div>
    </div>
    <div class="front-brand company-name"><span class="brand-dot"></span>Breezeway Climate</div>
    <ul class="contacts">
      <li><svg viewBox="0 0 12 12"><circle cx="6" cy="6" r="5" fill="none" stroke="var(--crimson)" stroke-width="1.3"/><path d="M4 3.5 L5 5 L4.6 5.6 Q5.5 7 6.6 7.4 L7.2 7 L8.5 8 L7.8 9 Q4 8.5 3.2 4.3 Z" fill="var(--crimson)"/></svg>555-214-6837</li>
      <li><svg viewBox="0 0 12 12"><rect x="1" y="2.5" width="10" height="7" fill="none" stroke="var(--crimson)"/><path d="M1 2.5 L6 7 L11 2.5" fill="none" stroke="var(--crimson)"/></svg>info@breezewayclimate.example</li>
      <li><svg viewBox="0 0 12 12"><circle cx="6" cy="6" r="5" fill="none" stroke="var(--crimson)"/><path d="M1 6 H11 M6 1 Q3 6 6 11 M6 1 Q9 6 6 11" fill="none" stroke="var(--crimson)" stroke-width="0.8"/></svg>www.BreezewayClimateLLC.example</li>
    </ul>
    <address class="address">PO box 618<br>Millbrook NJ 07999</address>
  </section>

  <section class="card card-back" aria-label="Card back">
    <div class="back-brand company-name"><span class="brand-dot"></span>Breezeway Climate</div>
  </section>
</main>
</body>
</html>
```